Poster Design Project

About Us
Brimco is a company that specializes in providing communication solutions to the travel market. Our simple vision of “every hotel should have a mobile phone in the guest rooms”, led us to develop a path breaking cost effective mobile phone. With full integration capabilities with the hotels property management system, location based marketing, user locator and other features, this product is unique in addressing the hospitality segment.
Product Placement
The Brimco mobile will be placed in the hotel room on an A4 Sized transparent stand (the transparent stand is attached for your reference. If you notice, the phone will be placed in the jacket on the bottom left and in another jacket on the bottom right will be the brochure. So effectively, the design space available on the A4 brochure is only 60% of the space). The designed poster that we wish designed will be inserted in the A4 sized acrylic stand. The stand would typically be on the bedside table or on the study table of the hotel room. The A4 design should be bright and vibrant in keeping with our logo colors.
Attached is our logo. Also attached is the symbol of our phone that could be used innovatively on the brochure if you think it helps.
Attached is the content for the poster.
Reason: Feedback from the management team got delayed, hence the extension. Thanks
Reason: The delay is in the content finalization.

```html
<!DOCTYPE html>
<html lang="en">
<head>
<meta charset="utf-8">
<title>Brimco – Keep Talking</title>
<link rel="stylesheet" href="https://fonts.googleapis.com/css2?family=PT+Sans:ital,wght@0,400;0,700;1,400;1,700&display=swap">
<style>
  :root {
    --sky: #45a0d2;
    --amber: #e0963d;
    --ink: #111111;
    --slate: #3a3a3a;
    --paper: #ffffff;
    --device-dark: #1c1d20;
    --device-mid: #55585e;
  }
  html, body {
    margin: 0;
    padding: 0;
    width: 849px;
    height: 1200px;
    overflow: hidden;
    background: var(--sky);
  }
  .poster {
    display: block;
    width: 849px;
    height: 1200px;
    font-family: "PT Sans", sans-serif;
  }
  .bubble { fill: var(--paper); stroke: var(--amber); stroke-width: 22; stroke-linejoin: round; }
  .brand-dot { fill: var(--amber); }
  .brand-name { font-weight: 700; font-size: 170px; fill: var(--amber); letter-spacing: -4px; }
  .headline { font-weight: 700; font-style: italic; font-size: 43px; fill: var(--amber); }
  .headline .stress { font-size: 50px; }
  .perk-ring { fill: var(--amber); }
  .perk-core { fill: var(--ink); }
  .perk-mark { fill: var(--amber); }
  .perk-text { font-style: italic; font-size: 28px; fill: var(--ink); }
  .signoff-name { font-weight: 700; font-style: italic; font-size: 27px; fill: var(--amber); }
  .signoff-line { font-weight: 700; font-style: italic; font-size: 27px; fill: var(--slate); }
  .tag-box { fill: var(--paper); stroke: var(--amber); stroke-width: 8; }
  .tag-text { font-style: italic; font-size: 21px; fill: var(--ink); }
  .footnote { font-style: italic; font-size: 25px; fill: var(--paper); }
</style>
</head>
<body>
<svg class="poster" viewBox="0 0 990 1400" xmlns="http://www.w3.org/2000/svg">
  <defs>
    <linearGradient id="deviceTone" x1="0" y1="0" x2="0" y2="1">
      <stop offset="0" stop-color="var(--device-mid)"/>
      <stop offset="1" stop-color="var(--device-dark)"/>
    </linearGradient>
  </defs>

  <rect width="990" height="1400" fill="var(--sky)"/>

  <path class="bubble" d="M100 60 H890 Q935 60 935 105 V735 Q935 775 890 775 H470 L582 1075 L265 878 H105 Q62 878 62 835 V105 Q62 60 100 60 Z"/>

  <g class="brand">
    <circle class="brand-dot" cx="232" cy="222" r="122"/>
    <text class="brand-name" x="388" y="282">Brimco</text>
  </g>

  <text class="headline" x="105" y="418">Pick up this phone <tspan class="stress">NOW</tspan>, to keep talking…</text>

  <g class="perks">
    <g transform="translate(153 478)">
      <circle class="perk-ring" r="26"/><circle class="perk-core" r="19"/>
      <rect class="perk-mark" x="-13" y="-2.5" width="26" height="5"/><rect class="perk-mark" x="-2.5" y="-13" width="5" height="26"/>
    </g>
    <text class="perk-text" x="197" y="488">SAVE 80% on international roaming</text>

    <g transform="translate(153 548)">
      <circle class="perk-ring" r="26"/><circle class="perk-core" r="19"/>
      <rect class="perk-mark" x="-13" y="-2.5" width="26" height="5"/><rect class="perk-mark" x="-2.5" y="-13" width="5" height="26"/>
    </g>
    <text class="perk-text" x="197" y="558">Get a LOCAL number</text>

    <g transform="translate(153 618)">
      <circle class="perk-ring" r="26"/><circle class="perk-core" r="19"/>
      <rect class="perk-mark" x="-13" y="-2.5" width="26" height="5"/><rect class="perk-mark" x="-2.5" y="-13" width="5" height="26"/>
    </g>
    <text class="perk-text" x="197" y="628">60 FREE minutes of international Calls</text>

    <g transform="translate(153 688)">
      <circle class="perk-ring" r="26"/><circle class="perk-core" r="19"/>
      <rect class="perk-mark" x="-13" y="-2.5" width="26" height="5"/><rect class="perk-mark" x="-2.5" y="-13" width="5" height="26"/>
    </g>
    <text class="perk-text" x="197" y="698">60 FREE minutes of local calls</text>

    <g transform="translate(153 758)">
      <circle class="perk-ring" r="26"/><circle class="perk-core" r="19"/>
      <rect class="perk-mark" x="-12" y="-8" width="24" height="5"/><rect class="perk-mark" x="-12" y="3" width="24" height="5"/>
    </g>
    <text class="perk-text" x="197" y="768">499 BHT</text>
  </g>

  <text x="890" y="738" text-anchor="end"><tspan class="signoff-name">Brimco</tspan><tspan class="signoff-line"> Keep Talking.</tspan></text>

  <g class="tags">
    <rect class="tag-box" x="72" y="998" width="260" height="60" rx="16"/>
    <text class="tag-text" x="91" y="1036">Itemized bill on checkout</text>
    <rect class="tag-box" x="72" y="1091" width="348" height="60" rx="16"/>
    <text class="tag-text" x="91" y="1129">Flexible tariff plans to choose from</text>
    <rect class="tag-box" x="72" y="1184" width="224" height="60" rx="16"/>
    <text class="tag-text" x="91" y="1222">Excellent call quality</text>
  </g>

  <rect role="img" aria-label="Photo of a black smartphone with a keyboard, the hotel room handset" x="612" y="815" width="303" height="500" rx="55" fill="url(#deviceTone)"/>

  <text class="footnote" x="90" y="1334">Refer to the brochure for more details</text>
</svg>
</body>
</html>
```